hi all

Im after a new age looking business card with my company logo on it

must include these details, I would like the PH and Email to be symbols

If the colours used for card could be kept within the colours used in logo that I have supplied that would be great, if another colour is to be used dark grey would be ok. no light bulbs etc thanks

Details below to be incorporated on card

Damian Holloway

Lic E871302

PH 0219647381

E info@brightvaleelectrical.example.nz

Domestic Commercial Industrial Electricians

```html
<!DOCTYPE html>
<html lang="en">
<head>
<meta charset="utf-8">
<title>Brightvale Electrical – Business Card</title>
<link href="https://fonts.googleapis.com/css2?family=Roboto:wght@400;500;700;900&display=swap" rel="stylesheet">
<style>
  :root {
    --page-bg: #e9e9e9;
    --card-white: #f7f7f7;
    --charcoal: #222222;
    --brand-blue: #0a72bb;
    --ink-black: #111111;
    --text-white: #ffffff;
    --pattern-tint: #e6eef5;
  }
  * { margin: 0; padding: 0; box-sizing: border-box; }
  html, body {
    width: 1200px; height: 900px; overflow: hidden;
    background: var(--page-bg);
    font-family: "Roboto", Arial, sans-serif;
  }
  .canvas { position: relative; width: 1200px; height: 900px; }
  .card {
    position: absolute; left: 250px; width: 700px; height: 400px;
    overflow: hidden; background: var(--card-white);
    box-shadow: 0 6px 18px rgba(0,0,0,0.18);
  }
  .card--back { top: 33px; }
  .card--front { top: 467px; }

  /* Back side */
  .back-shapes { position: absolute; inset: 0; width: 700px; height: 400px; }
  .contact { position: absolute; left: 58px; top: 70px; color: var(--text-white); }
  .contact__name-row { display: flex; align-items: center; gap: 18px; margin-bottom: 46px; }
  .contact__name { font-weight: 900; font-size: 30px; line-height: 1.05; letter-spacing: 1px; }
  .contact__licence { font-size: 18px; font-weight: 500; letter-spacing: 2px; margin: 0 0 22px 62px; }
  .contact__line { display: flex; align-items: center; gap: 18px; margin-bottom: 18px; font-weight: 500; }
  .contact__phone { font-size: 20px; letter-spacing: 2.5px; }
  .contact__email { font-size: 14px; letter-spacing: 0.6px; }
  .icon-disc {
    width: 42px; height: 42px; border-radius: 50%;
    background: var(--text-white); display: flex; align-items: center; justify-content: center;
    flex: none;
  }
  .brand-lockup { position: absolute; display: flex; align-items: center; gap: 12px; }
  .brand-lockup--small { left: 430px; top: 170px; }
  .brand-dot { border-radius: 50%; background: var(--brand-blue); flex: none; }
  .brand-lockup--small .brand-dot { width: 26px; height: 26px; }
  .brand-name { color: var(--brand-blue); font-weight: 700; line-height: 1; }
  .brand-lockup--small .brand-name { font-size: 22px; letter-spacing: 1px; }

  /* Front side */
  .circuit-field {
    position: absolute; inset: 0;
    background: linear-gradient(160deg, var(--card-white) 0%, var(--pattern-tint) 55%, var(--card-white) 100%);
  }
  .brand-lockup--large { left: 0; right: 0; top: 130px; justify-content: center; gap: 18px; }
  .brand-lockup--large .brand-dot { width: 56px; height: 56px; }
  .brand-lockup--large .brand-name { font-size: 48px; letter-spacing: 2px; }
  .footer-band { position: absolute; left: 0; bottom: 0; width: 700px; height: 90px; }
  .tagline {
    position: absolute; left: 100px; right: 80px; bottom: 36px;
    color: var(--text-white); font-weight: 700; font-size: 21px; letter-spacing: 1.4px;
    text-align: center;
  }
</style>
</head>
<body>
<main class="canvas">

  <section class="card card--back" aria-label="Card back with contact details">
    <svg class="back-shapes" viewBox="0 0 700 400" aria-hidden="true">
      <polygon points="0,0 265,0 262,230 318,220 372,400 0,400" fill="var(--charcoal)"/>
      <polygon points="265,0 292,0 340,130 395,118 412,400 372,400 318,220 262,230" fill="var(--brand-blue)"/>
    </svg>

    <div class="contact">
      <div class="contact__name-row">
        <span class="icon-disc">
          <svg width="22" height="22" viewBox="0 0 24 24" aria-hidden="true">
            <circle cx="12" cy="8" r="5" fill="var(--charcoal)"/>
            <path d="M3 22c0-5 4-8 9-8s9 3 9 8z" fill="var(--charcoal)"/>
          </svg>
        </span>
        <div class="contact__name">Damian<br>Holloway</div>
      </div>
      <p class="contact__licence">Lic E871302</p>
      <div class="contact__line">
        <span class="icon-disc">
          <svg width="20" height="20" viewBox="0 0 24 24" aria-hidden="true">
            <path d="M6.6 10.8a15 15 0 0 0 6.6 6.6l2.2-2.2a1 1 0 0 1 1-.25 11.4 11.4 0 0 0 3.6.57 1 1 0 0 1 1 1V20a1 1 0 0 1-1 1A17 17 0 0 1 3 4a1 1 0 0 1 1-1h3.5a1 1 0 0 1 1 1c0 1.25.2 2.45.57 3.57a1 1 0 0 1-.25 1z" fill="var(--charcoal)"/>
          </svg>
        </span>
        <span class="contact__phone">0219647381</span>
      </div>
      <div class="contact__line">
        <span class="icon-disc">
          <svg width="20" height="20" viewBox="0 0 24 24" aria-hidden="true">
            <rect x="2" y="5" width="20" height="14" rx="1.5" fill="var(--charcoal)"/>
            <path d="M3 6l9 7 9-7" fill="none" stroke="var(--text-white)" stroke-width="1.6"/>
          </svg>
        </span>
        <span class="contact__email">info@brightvaleelectrical.example.nz</span>
      </div>
    </div>

    <div class="brand-lockup brand-lockup--small">
      <span class="brand-dot"></span>
      <span class="brand-name">BRIGHTVALE ELECTRICAL</span>
    </div>
  </section>

  <section class="card card--front" aria-label="Card front with company name">
    <div class="circuit-field" role="img" aria-label="Faint light blue circuit-line background pattern"></div>

    <div class="brand-lockup brand-lockup--large">
      <span class="brand-dot"></span>
      <span class="brand-name">BRIGHTVALE ELECTRICAL</span>
    </div>

    <svg class="footer-band" viewBox="0 0 700 90" aria-hidden="true">
      <rect x="0" y="28" width="700" height="6" fill="var(--ink-black)"/>
      <rect x="0" y="34" width="700" height="56" fill="var(--brand-blue)"/>
      <path d="M90 34 V14 a10 10 0 0 1 10 -10 H610 a10 10 0 0 1 10 10 V34 z" fill="var(--brand-blue)"/>
    </svg>
    <p class="tagline">Domestic Commercial Industrial Electricians</p>
  </section>

</main>
</body>
</html>
```